Postcard Designed to solicit rental competition

I need a postcard designed for Willow Crest Apartments, a residential complex in Radcliff, KY. with 1 & 2 BR unfurnished apts, 1 BR extended stay (furnished) apts and townhouses.
I'm looking to solicit residents in other area complexes, directing them to visit www.wc-homes.example or visit my complex. I have mailing list to select who I want to solicit.
My key points are:
1. Deal direct with owner for great rate and for best deal
2. Application fee waived by presenting this postcard
3. Flexible security deposit, based on credit score
4. Monthly free rent specials
5. Tenant referral specials
A have a logo I would like to include and pics available to use if helpful.
Updates
Dana.... That looks great. Great job. Please just confirm that the address (blank) lines on the address side are removed because I have labels to attached. If I understand the process, all I have to do is click on accept and it's done, so I will do that. Please just be sure the blank address lines are deleted.
Thanks again
Ray
Target Market(s)
Other rental apartment complexes
Industry/Entity Type
Residential
Look and feel
Each slider illustrates characteristics of the customer's brand and the style your logo design should communicate.

```html
<!DOCTYPE html>
<html lang="en">
<head>
<meta charset="utf-8">
<title>Willow Crest Apartments – Postcard</title>
<link href="https://fonts.googleapis.com/css2?family=Della+Respira&family=Open+Sans:wght@400;600&display=swap" rel="stylesheet">
<style>
  :root {
    --brand-red: #b3222b;
    --brand-red-dark: #8f1a21;
    --gold: #f2c318;
    --ink: #ffffff;
    --panel: rgba(40, 40, 44, 0.72);
    --paper: #f4f4f7;
    --backdrop: #e7e5e0;
    --photo-sky: #d9dfe6;
    --photo-brick: #8e4a3c;
    --photo-green: #5b7a3a;
    --photo-asphalt: #8a8c8e;
    --serif: "Della Respira", Georgia, serif;
    --sans: "Open Sans", Arial, sans-serif;
  }
  * { box-sizing: border-box; margin: 0; padding: 0; }
  html, body { width: 1200px; height: 800px; overflow: hidden; }
  body {
    background: var(--backdrop);
    position: relative;
    font-family: var(--serif);
  }
  .postcard {
    position: absolute;
    top: 220px;
    width: 550px;
    height: 350px;
    overflow: hidden;
    box-shadow: 0 4px 14px rgba(0,0,0,0.18);
  }
  .postcard--back { left: 35px; background: var(--paper); }
  .postcard--front { left: 615px; }

  /* shared title ribbon */
  .title-ribbon {
    position: absolute;
    top: 0;
    right: 0;
    height: 44px;
    padding: 0 26px 0 46px;
    background: var(--brand-red);
    clip-path: polygon(0 0, 100% 0, 100% 100%, 40px 100%);
    color: var(--ink);
    font-size: 24px;
    line-height: 44px;
    white-space: nowrap;
  }

  /* back side */
  .back-photo {
    position: absolute;
    left: 0; top: 120px;
    width: 300px; height: 230px;
    background: linear-gradient(180deg, #d8dde2 0%, #c9c2bc 45%, #a7a7a8 100%);
  }
  .back-intro {
    position: absolute;
    top: 56px; left: 70px; right: 14px;
    color: var(--brand-red);
    font-size: 15px;
    line-height: 1.3;
    text-align: center;
  }
  .perks {
    position: absolute;
    left: 36px; top: 150px;
    width: 270px;
    padding: 14px 16px 14px 12px;
    background: var(--panel);
    border-radius: 22px;
    list-style: none;
    color: var(--ink);
  }
  .perks li {
    display: flex;
    align-items: flex-start;
    gap: 8px;
    font-size: 13.5px;
    line-height: 1.2;
    margin-bottom: 7px;
  }
  .perks li:last-child { margin-bottom: 0; }
  .perks li span { text-align: center; flex: 1; }
  .perks .tick { flex: 0 0 30px; width: 30px; height: 22px; }

  /* front side */
  .front-photo {
    position: absolute;
    inset: 0 0 48px 0;
    background:
      linear-gradient(180deg, var(--photo-sky) 0%, var(--photo-sky) 18%, transparent 18%),
      linear-gradient(180deg, #a85a48 18%, var(--photo-brick) 60%, var(--photo-asphalt) 75%, #9a9c9e 100%);
  }
  .front-photo::before {
    content: "";
    position: absolute;
    left: 0; top: 0; width: 90px; height: 75%;
    background: var(--photo-green);
    opacity: 0.8;
  }
  .pill {
    position: absolute;
    top: 138px;
    height: 92px;
    background: var(--panel);
    border-radius: 46px;
    display: flex;
    align-items: center;
  }
  .pill--best { left: -40px; width: 220px; padding-left: 48px; }
  .pill--visit { left: 188px; width: 330px; padding-left: 24px; }
  .pill__lead { font-size: 40px; margin-right: 12px; }
  .pill--best .pill__lead { color: var(--ink); }
  .pill--visit .pill__lead { color: var(--gold); }
  .pill__stack { font-size: 17px; line-height: 1.05; color: var(--ink); }
  .pill--visit .pill__stack { color: var(--gold); font-size: 18px; line-height: 1.2; }
  .contact-band {
    position: absolute;
    left: 0; right: 0; bottom: 0;
    height: 48px;
    background: var(--brand-red);
    color: var(--ink);
    font-family: var(--sans);
    font-size: 10px;
    text-align: center;
    padding-top: 8px;
  }
  .contact-band address { font-style: normal; margin-bottom: 7px; }
  .contact-band ul {
    list-style: none;
    display: flex;
    justify-content: space-between;
    padding: 0 22px;
    font-size: 9.5px;
  }
</style>
</head>
<body>

<section class="postcard postcard--back" aria-label="Postcard back">
  <div class="back-photo" role="img" aria-label="Photo of the apartment building, faded into the card"></div>
  <h2 class="title-ribbon">Willow Crest Apartments</h2>
  <p class="back-intro">Residential complex in Radcliff, KY. with 1 &amp; 2 BR unfurnished apts, 1 BR extended stay (furnished) apts and townhouses.</p>
  <ul class="perks">
    <li><svg class="tick" viewBox="0 0 30 22"><path d="M3 12 L11 19 L28 3" fill="none" stroke="#c8232c" stroke-width="4" stroke-linecap="round" stroke-linejoin="round"/></svg><span>Deal direct with owner for great rate and for best deal</span></li>
    <li><svg class="tick" viewBox="0 0 30 22"><path d="M3 12 L11 19 L28 3" fill="none" stroke="#c8232c" stroke-width="4" stroke-linecap="round" stroke-linejoin="round"/></svg><span>Application fee waived by presenting this postcard</span></li>
    <li><svg class="tick" viewBox="0 0 30 22"><path d="M3 12 L11 19 L28 3" fill="none" stroke="#c8232c" stroke-width="4" stroke-linecap="round" stroke-linejoin="round"/></svg><span>Flexible security deposit, based on credit score</span></li>
    <li><svg class="tick" viewBox="0 0 30 22"><path d="M3 12 L11 19 L28 3" fill="none" stroke="#c8232c" stroke-width="4" stroke-linecap="round" stroke-linejoin="round"/></svg><span>Monthly free rent specials</span></li>
    <li><svg class="tick" viewBox="0 0 30 22"><path d="M3 12 L11 19 L28 3" fill="none" stroke="#c8232c" stroke-width="4" stroke-linecap="round" stroke-linejoin="round"/></svg><span>Tenant referral specials</span></li>
  </ul>
</section>

<section class="postcard postcard--front" aria-label="Postcard front">
  <div class="front-photo" role="img" aria-label="Photo of the red brick apartment complex with trees and parked cars"></div>
  <h1 class="title-ribbon">Willow Crest Apartments</h1>
  <div class="pill pill--best">
    <span class="pill__lead">Best</span>
    <span class="pill__stack">Location<br>Choice<br>Value</span>
  </div>
  <div class="pill pill--visit">
    <span class="pill__lead">Visit</span>
    <span class="pill__stack">www.wc-homes.example<br>Or our complex</span>
  </div>
  <footer class="contact-band">
    <address>Willow Crest Apartments - 48 Meadow Lane - Radcliff, KY 40160</address>
    <ul>
      <li>Phone: 270.555.0146</li>
      <li>Fax: 270.555.0147</li>
      <li>Cell: 270.555.0182</li>
      <li>Email: leasing@wc-homes.example</li>
    </ul>
  </footer>
</section>

</body>
</html>
```